Kosmetikbroschüre
Zielgruppe
Kosmetik- und Wimpernstudio.
Professionelles Studio. klare Linie.
Wir bieten Kosmetikbehandlungen,Körperbehandlungen Wimpernverlängerung, Nageldesign, Enthaarung, Tanning, Fußpflege an.
Arbeiten mit den Firmen
Munta, RK Beauty, Verimunto, vivo Dorna, parak und Honigwachs Port zusammen.
www.lumira-studio.de
Aufgabenstellung
Erstellung einer Broschüre inkl. Preisliste.
Außerdem eine Zusatzpreisliste extra als reinen Flyer in A6 Quadrat
Format Broschüre ca. A5 quer. Gerne Alternative. hab neulich auch A4 hoch, aber schmaler als normales A4 gesehen... Sah ebenfalls sehr schön aus
Es gibt eine "alte" Broschüre, die optimiert werden könnte. Gerne freue ich mich aber auch über neue Ideen.
Hier sind bereits Behandlung integriert, fehlen jedoch noch welche.
Ideal wäre es, wenn die Daten dann im Indesign geliefert werden zum selbst weiter bearbeiten bzw. Texte einzufüllen....

```html
<!DOCTYPE html>
<html lang="de">
<head>
<meta charset="utf-8">
<title>Lumira – Broschüre Titelseite</title>
<link rel="stylesheet" href="https://fonts.googleapis.com/css2?family=Raleway:wght@300;400;500&family=Oswald:wght@200&display=swap">
<style>
  :root {
    --paper: #e6e5e6;
    --plum: #8c3e8e;
    --band-start: #a3659e;
    --band-end: #d2b8d6;
    --rose-text: #df5f9b;
    --grey-text: #9a9a9a;
    --heading-grey: #8d8a8a;
    --panel: rgba(255, 246, 242, 0.5);
    --thumb-line: #9b4a9c;
  }
  * { margin: 0; padding: 0; box-sizing: border-box; }
  html, body { width: 1200px; height: 801px; overflow: hidden; background: var(--paper); }
  .cover { position: relative; width: 1200px; height: 801px; background: var(--paper); font-family: "Raleway", sans-serif; }
  .cover-art { position: absolute; inset: 0; }
  .service-panel {
    position: absolute; left: 780px; top: 21px; width: 392px; height: 397px;
    background: var(--panel);
    border-radius: 70px 0 70px 0;
    padding: 72px 0 0 92px;
  }
  .service-panel h2 {
    font-family: "Oswald", sans-serif; font-weight: 200; font-size: 24px;
    letter-spacing: 8px; color: var(--heading-grey); line-height: 28px; margin-bottom: 14px;
  }
  .service-list { list-style: none; }
  .service-list li {
    font-weight: 300; font-size: 17.5px; color: var(--rose-text);
    line-height: 31.4px; letter-spacing: 0.1px;
  }
  .brand { position: absolute; left: 77px; top: 580px; }
  .brand-name {
    font-weight: 500; font-size: 58px; color: var(--plum);
    letter-spacing: 24px; line-height: 1;
  }
  .brand-tagline {
    margin-top: 12px; font-weight: 400; font-size: 24px;
    color: var(--grey-text); letter-spacing: 0.2px;
  }
  .thumb {
    position: absolute; top: 540px; width: 150px; height: 151px;
    border: 1.5px solid var(--thumb-line);
    border-radius: 40px 0 40px 0;
  }
  .thumb--eye {
    left: 606px;
    background:
      radial-gradient(ellipse 40% 30% at 40% 32%, #f3e3da 0%, transparent 100%),
      radial-gradient(ellipse 60% 50% at 75% 80%, #d29c82 0%, transparent 100%),
      linear-gradient(135deg, #f6ebe5, #e6bca6 55%, #cf967d);
  }
  .thumb--massage {
    left: 778px;
    background:
      radial-gradient(ellipse 45% 35% at 70% 55%, #5a4037 0%, transparent 100%),
      radial-gradient(ellipse 70% 40% at 30% 75%, #d8ab93 0%, transparent 100%),
      linear-gradient(170deg, #f6f2f0 30%, #e2c0ad 65%, #f1ebe8);
  }
  .thumb--foot {
    left: 949px;
    background:
      radial-gradient(ellipse 70% 35% at 50% 55%, #ecc4b6 0%, transparent 100%),
      linear-gradient(160deg, #f7f3f2, #f1dcd4 55%, #f5eeec);
  }
</style>
</head>
<body>
<main class="cover">
  <svg class="cover-art" width="1200" height="801" viewBox="0 0 1200 801" xmlns="http://www.w3.org/2000/svg">
    <defs>
      <linearGradient id="facialTone" x1="0" y1="0" x2="1" y2="1">
        <stop offset="0" stop-color="#f2e6e2"/>
        <stop offset="0.5" stop-color="#f7f3f1"/>
        <stop offset="1" stop-color="#e9d0c8"/>
      </linearGradient>
      <radialGradient id="facialWarm" cx="0.45" cy="0.45" r="0.55">
        <stop offset="0" stop-color="#f9f6f5"/>
        <stop offset="0.7" stop-color="#efdcd6" stop-opacity="0.6"/>
        <stop offset="1" stop-color="#e3c2b6" stop-opacity="0"/>
      </radialGradient>
      <linearGradient id="waxingTone" x1="0" y1="0" x2="1" y2="1">
        <stop offset="0" stop-color="#f7eeea"/>
        <stop offset="0.4" stop-color="#efc8b3"/>
        <stop offset="0.7" stop-color="#e4aa8d"/>
        <stop offset="1" stop-color="#f4dcd3"/>
      </linearGradient>
      <radialGradient id="waxingLight" cx="0.25" cy="0.35" r="0.45">
        <stop offset="0" stop-color="#fbf6f3"/>
        <stop offset="1" stop-color="#fbf6f3" stop-opacity="0"/>
      </radialGradient>
      <linearGradient id="petalTone" x1="0" y1="0" x2="1" y2="0">
        <stop offset="0" stop-color="#f4e6e4" stop-opacity="0"/>
        <stop offset="0.5" stop-color="#f2d3d4"/>
        <stop offset="1" stop-color="#efc8cc"/>
      </linearGradient>
      <linearGradient id="bandTone" x1="0" y1="0" x2="1" y2="0">
        <stop offset="0" stop-color="var(--band-start)"/>
        <stop offset="0.6" stop-color="#b584b5"/>
        <stop offset="1" stop-color="var(--band-end)"/>
      </linearGradient>
    </defs>
    <g role="img" aria-label="Foto: Gesichtsbehandlung mit Maske">
      <rect x="0" y="0" width="347" height="420" fill="url(#facialTone)"/>
      <rect x="0" y="0" width="347" height="420" fill="url(#facialWarm)"/>
    </g>
    <g role="img" aria-label="Foto: Haarentfernung mit Wachsstreifen am Bein, Rosenblätter">
      <rect x="347" y="0" width="853" height="480" fill="url(#waxingTone)"/>
      <rect x="347" y="0" width="853" height="480" fill="url(#waxingLight)"/>
      <rect x="700" y="400" width="500" height="80" fill="url(#petalTone)"/>
    </g>
    <path class="paper-area" fill="var(--paper)"
      d="M0,415 C300,408 500,414 720,440 C900,465 1050,477 1200,477 L1200,801 L0,801 Z"/>
    <path class="wave-band" fill="url(#bandTone)"
      d="M0,389 C300,382 500,390 720,418 C900,446 1050,466 1200,467 L1200,477 C1050,477 900,465 720,440 C500,414 300,408 0,415 Z"/>
  </svg>

  <section class="service-panel">
    <h2>BEAUTYSTUDIO</h2>
    <ul class="service-list">
      <li>KOSMETIKBEHANDLUNGEN</li>
      <li>KÖRPERBEHANDLUNGEN</li>
      <li>WIMPERNVERLÄNGERUNG</li>
      <li>NAGELDESIGN</li>
      <li>ENTHAARUNG</li>
      <li>TANNING</li>
      <li>FUSSPFLEGE</li>
    </ul>
  </section>

  <header class="brand">
    <h1 class="brand-name">lumira</h1>
    <p class="brand-tagline">SCHÖNHEIT UND WOHLGEFÜHL</p>
  </header>

  <div class="thumb thumb--eye" role="img" aria-label="Foto: Augenpartie mit Wimpern"></div>
  <div class="thumb thumb--massage" role="img" aria-label="Foto: Rückenmassage"></div>
  <div class="thumb thumb--foot" role="img" aria-label="Foto: gepflegter Fuß"></div>
</main>
</body>
</html>
```